indoor tennis and sports center( club)

we need a logo for a new business venture, it will be for business cards and for presentations.
presentations for potential investors and authorities.
the design needs to communicate the sport and a community of tennis players
the center includes a tennis academy, and sports club with training sessions for all ages

Project Deadline Extended
Reason: so that I can get some more feedback on my side as to te design we want

Target Market(s)

potential investors or partners

Industry/Entity Type

Business

Contact Information for Business Card

i need the name of the club
names of the partners
slogan" changing lives through tennis" on the front
the clubs three main goals are ports education , academy and a community club

Colors
3176b5
33b8a4
fbee3d
0dac94
acd036

Requirements
Must have
• a strong logo
• names of the partners
• web site and email address
• tel number
Nice to have
• a connection between the different aspects of the club

```html
<!DOCTYPE html>
<html lang="en">
<head>
<meta charset="utf-8">
<title>Baseline Hall – Business Card</title>
<link href="https://fonts.googleapis.com/css2?family=Lato:wght@400;700&display=swap" rel="stylesheet">
<style>
  :root {
    --stage: #232323;
    --card: #ffffff;
    --ink: #4a5850;
    --lime: #a9bf2f;
    --rule: #5d6a62;
    --stone: #aeb8b1;
  }
  html, body {
    margin: 0;
    width: 1189px;
    height: 1200px;
    overflow: hidden;
    background: var(--stage);
    font-family: "Lato", Arial, sans-serif;
  }
  .card {
    position: absolute;
    left: 171px;
    width: 856px;
    height: 488px;
    background: var(--card);
    border-radius: 38px;
  }
  .card--front { top: 67px; }
  .card--back { top: 626px; }

  .brand {
    position: absolute;
    display: flex;
    align-items: center;
    gap: 14px;
    color: var(--ink);
    font-weight: 700;
    white-space: nowrap;
  }
  .brand__dot {
    border-radius: 50%;
    background: var(--lime);
    flex: none;
  }
  .card--front .brand {
    left: 0; right: 0;
    top: 190px;
    justify-content: center;
    font-size: 50px;
  }
  .card--front .brand__dot { width: 34px; height: 34px; }

  .slogan {
    position: absolute;
    left: 0; right: 0;
    top: 405px;
    text-align: center;
    font-size: 26px;
    font-weight: 700;
    color: var(--ink);
  }

  .card--back .brand {
    left: 40px;
    top: 225px;
    font-size: 34px;
    gap: 10px;
  }
  .card--back .brand__dot { width: 24px; height: 24px; }

  .divider {
    position: absolute;
    left: 410px;
    top: 104px;
    width: 2px;
    height: 282px;
    background: var(--rule);
  }
  .person {
    position: absolute;
    left: 453px;
    top: 98px;
  }
  .person__name {
    margin: 0;
    font-size: 30px;
    font-weight: 700;
    color: var(--ink);
    line-height: 1;
  }
  .person__role {
    margin: 4px 0 0;
    font-size: 24px;
    color: var(--lime);
    line-height: 1;
  }
  .contacts {
    position: absolute;
    left: 453px;
    top: 216px;
    margin: 0;
    padding: 0;
    list-style: none;
  }
  .contacts li {
    display: flex;
    align-items: center;
    gap: 10px;
    height: 32px;
    font-size: 25px;
    color: var(--ink);
  }
  .contacts svg { width: 28px; height: 28px; flex: none; }
  .services {
    position: absolute;
    left: 453px;
    top: 345px;
    font-size: 25px;
    color: var(--ink);
    white-space: nowrap;
  }
</style>
</head>
<body>

<section class="card card--front">
  <div class="brand"><span class="brand__dot"></span>Baseline Hall</div>
  <p class="slogan">Changing lives through Tennis</p>
</section>

<section class="card card--back">
  <div class="brand"><span class="brand__dot"></span>Baseline Hall</div>
  <div class="divider"></div>
  <div class="person">
    <p class="person__name">MARA VELDEN</p>
    <p class="person__role">Owner</p>
  </div>
  <ul class="contacts">
    <li>
      <svg viewBox="0 0 28 28" aria-hidden="true"><circle cx="14" cy="14" r="14" fill="var(--lime)"/><path d="M10 7c1 0 2 3 2 4s-2 1-1 3 2 3 3 3 1-2 2-2 4 1 4 2-2 3-4 3c-4 0-10-6-10-10 0-2 3-3 4-3z" fill="#fff"/></svg>
      555 010 2040
    </li>
    <li>
      <svg viewBox="0 0 28 28" aria-hidden="true"><circle cx="14" cy="14" r="14" fill="var(--lime)"/><rect x="7" y="9" width="14" height="10" fill="none" stroke="#fff" stroke-width="1.6"/><path d="M7 9l7 6 7-6" fill="none" stroke="#fff" stroke-width="1.6"/></svg>
      hello@baselinehall.com
    </li>
    <li>
      <svg viewBox="0 0 28 28" aria-hidden="true"><circle cx="14" cy="14" r="14" fill="var(--lime)"/><g fill="none" stroke="#fff" stroke-width="1.4"><circle cx="14" cy="14" r="7"/><ellipse cx="14" cy="14" rx="3" ry="7"/><path d="M7 14h14M8.5 10.5h11M8.5 17.5h11"/></g></svg>
      www.baselinehall.com
    </li>
  </ul>
  <p class="services">Indoor club | Academy | Education</p>
</section>

</body>
</html>
```